Unique, Impressive, and Modern Business Card

Looking for a distinctive, unique business card. We are distributors of tire repairs supplies, tools, machinery, and chemicals. Our target market are tire repair shops, tire franchises, and mechanic shops. We would like our design to include tire characteristics, and use our business colors. Feel free to use all types design and printing options (emboss, spot uv, foil, etc) QR code may be applied, you can use different size business cards ( standard, square, rounded edge, colored edge, etc), all formats needed for printing, also editable for future changes

Target Market(s)

Automotive, Tire industries

Industry/Entity Type

Tire Industry (automotive)

Contact Information for Business Card

Business logo, business Name (Corvane Supply Inc), Name (Marcus Pellow), Position (President) Address (58 Fernhollow Lane, Brentwood NY 11742), Contact number (Company 1-855-302-4418, Cell 1-631-245-9073, email address (marcus.pellow@corvanesupply.com), URL (www.corvanesupply.com

Requirements
Must have
• Must include Business Colors (Black, Green, Blue, White) see sample website file
Nice to have
• emboss, spot uv, etc

```html
<!DOCTYPE html>
<html lang="en">
<head>
<meta charset="utf-8">
<title>Corvane Supply – Business Card</title>
<link rel="stylesheet" href="https://fonts.googleapis.com/css2?family=Source+Sans+3:wght@400;600;700&display=swap">
<style>
  :root {
    --ink: #111111;
    --card-black: #1a1a1a;
    --brand-blue: #3a4fa6;
    --white: #ffffff;
    --stage: #e9e9ec;
  }
  * { box-sizing: border-box; margin: 0; padding: 0; }
  html, body { width: 1200px; height: 912px; overflow: hidden; }
  body {
    background: var(--stage);
    font-family: "Source Sans 3", "Myriad Pro", Arial, sans-serif;
    position: relative;
  }
  .card {
    position: absolute;
    width: 540px;
    height: 309px;
    box-shadow: 0 10px 28px rgba(0,0,0,0.18);
    overflow: hidden;
  }

  /* Back side */
  .card-back { left: 40px; top: 301px; background: var(--card-black); }
  .back-texture {
    position: absolute; inset: 0;
    background: radial-gradient(circle at 60% 45%, #262626 0%, var(--card-black) 70%);
  }
  .back-brand {
    position: absolute; left: 300px; top: 134px;
    display: flex; align-items: center; gap: 10px;
  }
  .back-brand .mark {
    width: 40px; height: 40px; border-radius: 50%;
    background: var(--white);
  }
  .back-brand .name {
    color: var(--white); font-size: 21px; font-weight: 400;
    text-transform: uppercase; letter-spacing: -0.5px;
  }

  /* Front side */
  .card-front { left: 620px; top: 301px; background: var(--white); }
  .front-band { position: absolute; inset: 0; }
  .person {
    position: absolute; right: 34px; top: 22px; text-align: right;
  }
  .person .full-name {
    color: var(--brand-blue); font-weight: 700; font-size: 26px;
    text-transform: uppercase; letter-spacing: -0.8px; line-height: 1;
  }
  .person .role { color: var(--ink); font-size: 14px; margin-top: 2px; }
  .corner-tab {
    position: absolute; right: 0; top: 16px; width: 22px; height: 30px;
    background: var(--brand-blue);
  }
  .front-brand {
    position: absolute; left: 28px; top: 90px;
    display: flex; align-items: center; gap: 10px;
  }
  .front-brand .mark {
    width: 46px; height: 46px; border-radius: 50%; background: var(--ink);
  }
  .front-brand .name {
    color: var(--ink); font-size: 25px; font-weight: 400;
    text-transform: uppercase; letter-spacing: -0.8px;
  }
  .contact {
    position: absolute; left: 28px; top: 190px;
    color: var(--white); font-size: 14px; line-height: 1.22;
  }
  .contact .address { margin-bottom: 8px; }
  .contact li { list-style: none; display: flex; align-items: center; gap: 7px; }
  .contact svg { width: 11px; height: 11px; flex: none; fill: var(--white); }
</style>
</head>
<body>

  <section class="card card-back" aria-label="Card back">
    <div class="back-texture" role="img" aria-label="Embossed repeating brand mark pattern on black stock"></div>
    <div class="back-brand">
      <span class="mark"></span>
      <span class="name">Corvane Supply</span>
    </div>
  </section>

  <section class="card card-front" aria-label="Card front">
    <svg class="front-band" viewBox="0 0 540 309" width="540" height="309" aria-hidden="true">
      <path d="M0 182 H285 V140 H540 V296 H0 Z" fill="var(--brand-blue)"/>
      <circle cx="462" cy="214" r="80" fill="var(--white)"/>
      <rect x="462" y="214" width="78" height="82" fill="var(--brand-blue)"/>
      <circle cx="462" cy="214" r="62" fill="var(--ink)"/>
    </svg>
    <span class="corner-tab"></span>

    <div class="person">
      <p class="full-name">Marcus Pellow</p>
      <p class="role">President</p>
    </div>

    <div class="front-brand">
      <span class="mark"></span>
      <span class="name">Corvane Supply</span>
    </div>

    <div class="contact">
      <p class="address">58 Fernhollow Lane,<br>Halvern Falls VT 05732</p>
      <ul>
        <li><svg viewBox="0 0 12 12"><path d="M1 3 Q6 0 11 3 V5 H8 V4 H4 V5 H1 Z M2 6 H10 L11 11 H1 Z"/></svg>1-855-302-4418</li>
        <li><svg viewBox="0 0 12 12"><path d="M2 1 L4.5 1 L5.5 3.5 L4 4.8 Q5 7 7.2 8 L8.5 6.5 L11 7.5 V10 Q11 11 10 11 Q1 10 1 2 Q1 1 2 1 Z"/></svg>1-555-245-9073</li>
        <li><svg viewBox="0 0 12 12"><path d="M1 2.5 H11 V9.5 H1 Z M2 3.5 V8.5 H10 V3.5 L6 6.5 Z" fill-rule="evenodd"/></svg>marcus.pellow@corvanesupply.com</li>
        <li><svg viewBox="0 0 12 12"><circle cx="6" cy="6" r="5"/><path d="M1 6 H11 M6 1 V11" stroke="#3a4fa6" stroke-width="0.9"/></svg>www.corvanesupply.com</li>
      </ul>
    </div>
  </section>

</body>
</html>
```